Packaging design for children’s shampoo bar

A design that could be used on solid shampoo and soap wraps then amended for jar labels. The packaging needs to be bright and child-friendly. We have a logo and a pattern, but please feel free to change them. I think it needs to be brighter.

I would like each product to have an accent colour and for the shampoo I am thinking of blue/teal. This will be complemented by the body wash bar (pink) and toothpaste (orange).

The shampoo bar wrap needs to contain the following information:

Pippa & Pals logo
Shampoo Bar
100% natural
Vegan & Palm Oil-Free
Weight 85 g
Made in the U.K.

Ingredients: sodium hydroxide, prunus amygdalus dulcis oil, olea europaea oil, cocos nucifera oil, ricinus communis seed oil, simmondsia chinensia seed oil.

Contact details: Pippa & Pals, Marden Oakley House, London N7 4QB. Website: www.Pippa and pals.co.U.K.

Brand board is here: https://www.filevaultex.com/s/k8rw2tqumezbvyx/Photo%2003-07-2020%2C%2021%2040%2034.jpg?dl=0

Inspiration is here: https://kitemoorstudio.co.uk/collections/beauty-grooming/products/dog-shampoo-100-natural-vegan

These are the wraps we shall be using: https://www.brightwickpress.co.uk/soap-wrap

Thank you so much for your interest in this project!

Target Market(s)

Children 5-12 years.

Requirements
Must have
• Clean design. Lots of white with bright colours.

```html
<!DOCTYPE html>
<html lang="en">
<head>
<meta charset="utf-8">
<title>Pippa &amp; Pals Shampoo Bar Wrap</title>
<link href="https://fonts.googleapis.com/css2?family=Montserrat:wght@500;600;700&family=Nothing+You+Could+Do&display=swap" rel="stylesheet">
<style>
  :root {
    --bg: #b9b9b9;
    --paper: #f4f4f2;
    --paper-side: #eeeeec;
    --green: #2f9a4a;
    --band: #2e8f3f;
    --coral: #e8845a;
    --badge: #e8804c;
    --ink: #2b2b2b;
    --white: #ffffff;
    --rainbow-a: #f2c4c8;
    --rainbow-b: #bfe0ee;
    --leaf: #f6e3a2;
    --ape: #e58a63;
    --cat: #f0cf3a;
    --pangolin: #e8a6c6;
    --plant: #9fd3ea;
  }
  * { margin: 0; padding: 0; box-sizing: border-box; }
  html, body { width: 1200px; height: 1037px; overflow: hidden; background: var(--bg); }
  .canvas { position: relative; width: 1200px; height: 1037px; font-family: "Montserrat", sans-serif; }

  /* Side panel */
  .wrap-side {
    position: absolute; left: 135px; top: 113px; width: 110px; height: 808px;
    background: var(--paper-side); overflow: hidden;
  }
  .side-ground { position: absolute; left: 0; top: 0; width: 110px; height: 808px; }
  .side-brand {
    position: absolute; left: 50%; top: 150px;
    transform: translateX(-50%) rotate(180deg);
    writing-mode: vertical-rl;
    font-weight: 700; font-size: 30px; color: var(--coral); white-space: nowrap;
  }
  .side-title {
    position: absolute; left: 50%; top: 440px;
    transform: translateX(-50%) rotate(180deg);
    writing-mode: vertical-rl;
    font-weight: 700; font-size: 28px; line-height: 1.05; color: var(--green);
    text-align: center; white-space: nowrap;
  }

  /* Front panel */
  .wrap-front {
    position: absolute; left: 245px; top: 113px; width: 820px; height: 808px;
    background: var(--paper); overflow: hidden;
  }
  .art { position: absolute; border-radius: 40% 40% 20% 20%; }
  .art-rainbow { left: 59px; top: 74px; width: 140px; height: 133px; border-radius: 70px 70px 6px 6px;
    background: linear-gradient(180deg, var(--rainbow-a), var(--rainbow-b)); opacity: .8; }
  .art-leaf { left: 688px; top: 89px; width: 67px; height: 59px; background: var(--leaf); border-radius: 50%; }
  .brand-name {
    position: absolute; left: 0; right: 0; top: 150px; text-align: center;
    font-weight: 700; font-size: 68px; color: var(--coral); letter-spacing: 1px;
  }
  .product-title {
    position: absolute; left: 0; right: 0; top: 334px; text-align: center;
    font-weight: 700; font-size: 64px; color: var(--green); letter-spacing: .5px;
  }
  .product-claim {
    position: absolute; left: 0; right: 0; top: 410px; text-align: center;
    font-family: "Nothing You Could Do", cursive; font-size: 56px; color: var(--ink);
  }
  .product-tagline {
    position: absolute; left: 0; right: 0; top: 488px; text-align: center;
    font-weight: 600; font-size: 28px; color: var(--green);
  }
  .ground { position: absolute; left: 0; top: 0; width: 820px; height: 808px; }
  .art-ape { left: 55px; top: 567px; width: 86px; height: 109px; background: var(--ape); }
  .art-cat { left: 156px; top: 592px; width: 155px; height: 111px; background: var(--cat); border-radius: 30%; }
  .art-pangolin { left: 340px; top: 611px; width: 111px; height: 104px; background: var(--pangolin); border-radius: 50%; }
  .art-plant { left: 688px; top: 528px; width: 104px; height: 116px; background: var(--plant); border-radius: 50% 50% 10% 10%; }
  .weight-badge {
    position: absolute; left: 567px; top: 548px; width: 100px; height: 114px;
    background: var(--badge); border-radius: 8px; color: var(--white); text-align: center;
    padding-top: 24px;
  }
  .weight-label { font-size: 18px; font-weight: 500; line-height: 1; }
  .weight-value { font-size: 36px; font-weight: 600; line-height: 1.1; }
  .origin {
    position: absolute; left: 477px; top: 682px;
    font-weight: 600; font-size: 26px; color: var(--white);
  }
</style>
</head>
<body>
<div class="canvas">
  <section class="wrap-side">
    <svg class="side-ground" viewBox="0 0 110 808" aria-hidden="true">
      <path d="M0 700 C 40 705, 80 690, 110 680 L 110 808 L 0 808 Z" fill="var(--band)"/>
    </svg>
    <div class="side-brand">Pippa &amp; Pals</div>
    <p class="side-title">SHAMPOO<br>BAR</p>
  </section>

  <section class="wrap-front">
    <div class="art art-rainbow" role="img" aria-label="Pastel hand-drawn rainbow"></div>
    <div class="art art-leaf" role="img" aria-label="Small pale yellow leaf sprig"></div>

    <div class="brand-name">Pippa &amp; Pals</div>
    <h1 class="product-title">SHAMPOO BAR</h1>
    <p class="product-claim">100% Natural</p>
    <p class="product-tagline">Vegan &amp; Palm Oil-Free</p>

    <svg class="ground" viewBox="0 0 820 808" aria-hidden="true">
      <path d="M0 673 C 80 690, 150 700, 230 690 C 320 675, 380 650, 460 632 C 560 612, 680 625, 820 620 L 820 808 L 0 808 Z" fill="var(--band)"/>
    </svg>

    <div class="art art-ape" role="img" aria-label="Illustrated orange orangutan"></div>
    <div class="art art-cat" role="img" aria-label="Illustrated yellow spotted cheetah"></div>
    <div class="art art-pangolin" role="img" aria-label="Illustrated pink pangolin"></div>
    <div class="art art-plant" role="img" aria-label="Illustrated light blue aloe plant"></div>

    <div class="weight-badge">
      <div class="weight-label">Weight</div>
      <div class="weight-value">85G</div>
    </div>
    <p class="origin">Made in the U.K</p>
  </section>
</div>
</body>
</html>
```